Business Card Design

We need business cards designed incorporating our graphics/logo already used on our trucks. We are a small construction company that does everything from building new homes, additions, Kitchens, Baths, Decks, Hardwood Floors/Tile, all phases of construction. No job is too small. We pride ourselves on True Craftmanship/Customer Satisfaction, its what truly separates us from everyone else.

Industry/Entity Type

Construction

Contact Information for Business Card

Maple Ridge Renovations Lic#27KT51986400
342 51st Avenue Gull Harbor NJ 08100
(555)317-2984 Email: info@mapleridgellc.example
Paul Tremondale

```html
<!DOCTYPE html>
<html lang="en">
<head>
<meta charset="utf-8">
<title>Maple Ridge Renovations – Business Card</title>
<link rel="stylesheet" href="https://fonts.googleapis.com/css2?family=Arimo:wght@400;700&display=swap">
<style>
  :root {
    --backdrop: #0f4f8c;
    --card-white: #fbfbfa;
    --sand: #e1b37c;
    --sky: #cfe6f3;
    --sky-deep: #9fcbe6;
    --ink: #262522;
    --banner: #1d1d1d;
    --on-dark: #ffffff;
  }
  * { box-sizing: border-box; margin: 0; padding: 0; }
  html, body { width: 1200px; height: 1087px; overflow: hidden; }
  body {
    background: var(--backdrop);
    font-family: "Arimo", Arial, sans-serif;
    color: var(--ink);
    position: relative;
  }
  .card {
    position: absolute;
    top: 54px;
    width: 526px;
    height: 924px;
    overflow: hidden;
  }
  .card-front { left: 52px; background: var(--card-white); border-radius: 50px 0 0 0; }
  .card-back { left: 621px; background: var(--sand); border-radius: 50px 0 50px 0; }

  .brand-name {
    position: absolute; left: 0; width: 100%; text-align: center;
    font-weight: 700; text-transform: uppercase; color: var(--ink);
  }
  .brand-name span { display: block; }

  /* front */
  .front-band {
    position: absolute; left: 0; top: 270px; width: 100%; height: 385px;
    background: linear-gradient(180deg, var(--sky) 0%, #eaf4fa 40%, var(--sky-deep) 60%, var(--sky) 68%);
  }
  .phone-banner { position: absolute; left: 6px; top: 15px; width: 317px; height: 47px; }
  .phone-banner svg { position: absolute; inset: 0; }
  .phone-banner span {
    position: absolute; inset: 0; display: flex; align-items: center; justify-content: center;
    padding-left: 16px; color: var(--on-dark); font-weight: 700; font-size: 25px; letter-spacing: 1px;
  }
  .plane-art {
    position: absolute; left: 334px; top: 0; width: 186px; height: 112px;
    background: linear-gradient(135deg, #e04a3c, #c9d9e4 70%);
    opacity: .75; border-radius: 8px;
  }
  .front-band .brand-name { top: 68px; font-size: 62px; line-height: 66px; }
  .front-sand {
    position: absolute; left: 0; top: 270px; width: 100%; height: 115px;
    background: var(--sand);
    border-radius: 60% 40% 0 0 / 14px 10px 0 0;
  }
  .services {
    position: absolute; left: 40px; top: 10px; list-style: none;
    color: var(--on-dark); font-weight: 700; font-size: 20px; letter-spacing: .5px; line-height: 26px;
  }
  .services li { position: relative; padding-left: 18px; margin-bottom: 11px; }
  .services li::before {
    content: ""; position: absolute; left: 0; top: 8px; width: 11px; height: 11px;
    border-radius: 50%; background: var(--ink);
  }
  .crew-art {
    position: absolute; left: 388px; bottom: 0; width: 125px; height: 112px;
    background: linear-gradient(180deg, #f0c94a 0%, #3c4f8f 45%, #2e3d72 100%);
    border-radius: 40px 40px 0 0; opacity: .85;
  }

  /* back */
  .person-name {
    position: absolute; top: 198px; width: 100%; text-align: center;
    font-weight: 700; font-size: 33px; line-height: 40px; letter-spacing: .5px;
  }
  .back-band {
    position: absolute; left: 0; top: 419px; width: 100%; height: 250px;
    background: linear-gradient(180deg, #ffffff 0%, #ffffff 8%, var(--sky) 20%, #eef6fb 40%, var(--sky-deep) 62%, var(--sky) 72%, #ffffff 78%);
  }
  .back-band .brand-name { top: 0; font-size: 62px; line-height: 68px; }
  .license {
    position: absolute; top: 208px; width: 100%; text-align: center;
    font-weight: 700; font-size: 30px; line-height: 36px;
  }
  .contact { position: absolute; left: 52px; top: 691px; list-style: none; font-size: 28px; }
  .contact li { display: flex; align-items: flex-start; gap: 14px; margin-bottom: 12px; line-height: 37px; }
  .contact svg { flex: 0 0 24px; margin-top: 7px; }
</style>
</head>
<body>
  <section class="card card-front">
    <div class="front-band">
      <div class="plane-art" role="img" aria-label="Illustration of a red biplane towing a banner over the sky"></div>
      <div class="phone-banner">
        <svg viewBox="0 0 317 47" width="317" height="47" aria-hidden="true">
          <polygon points="0,6 317,0 317,47 0,45 22,26" fill="var(--banner)"/>
        </svg>
        <span>(555) 317 - 2984</span>
      </div>
      <h1 class="brand-name"><span>Maple</span><span>Ridge</span><span>Renovations</span></h1>
      <div class="front-sand">
        <ul class="services">
          <li>REMODELING</li>
          <li>DECKS</li>
          <li>ADDITIONS</li>
        </ul>
        <div class="crew-art" role="img" aria-label="Illustration of two builders in hard hats beside a wooden sign"></div>
      </div>
    </div>
  </section>

  <section class="card card-back">
    <h2 class="person-name">PAUL TREMONDALE</h2>
    <div class="back-band">
      <p class="brand-name"><span>Maple</span><span>Ridge</span><span>Renovations</span></p>
      <p class="license">LIC#27KT51986400</p>
    </div>
    <ul class="contact">
      <li>
        <svg width="24" height="24" viewBox="0 0 24 24" aria-hidden="true"><path d="M12 1a8 8 0 0 0-8 8c0 6 8 14 8 14s8-8 8-14a8 8 0 0 0-8-8zm0 11a3 3 0 1 1 0-6 3 3 0 0 1 0 6z" fill="var(--ink)"/></svg>
        <span>342 51st Avenue Gull Harbor<br>NJ 08100</span>
      </li>
      <li>
        <svg width="24" height="24" viewBox="0 0 24 24" aria-hidden="true"><circle cx="12" cy="12" r="11" fill="var(--ink)"/><path d="M9 6l2 3-1.5 1.5c.6 1.6 1.9 2.9 3.5 3.5L14.5 12.5l3 2-1 2.5c-4.5 0-9-4.5-9-9z" fill="var(--sand)"/></svg>
        <span>(555)317-2984</span>
      </li>
      <li>
        <svg width="24" height="24" viewBox="0 0 24 24" aria-hidden="true"><rect x="2" y="5" width="20" height="14" rx="1.5" fill="none" stroke="var(--ink)" stroke-width="2.2"/><path d="M2.5 6l9.5 7 9.5-7M2.5 18l7-6M21.5 18l-7-6" fill="none" stroke="var(--ink)" stroke-width="2"/></svg>
        <span>info@mapleridgellc.example</span>
      </li>
    </ul>
  </section>
</body>
</html>
```